New Hotel Showcase Website

We plan to launch a website called www.brindlestays.net which showcases the world’s best new hotels. We want a mock up for 2 pages: the homepage (page 1) and the individual hotel page (page 2). We are looking for a design which combines simplicity while highlighting images/features of the hotel. Because the theme of the site is new hotels it is important that the design somehow emphasizes the age of each hotel listed – both on the homepage and then on the individual hotel page.

NOTE: WE WANT A CREATIVE, NEW APPROACH TO DISPLAYING HOTELS. NOT JUST A COPY OF CURRENT HOTEL WEBSITES.

The design should consider unique and creative ways of helping users to navigate the homepage (page 1) based on the age, location or style of the hotel they are interested in. The individual hotel page(page 2) can be more standard by clearly setting out hotel photos, feature lists, reviews, contact details and potential discounts. There is no booking system needed as this is not a hotel booking website.

The design should ideally be compatible with a content management system such as Page Loom. In terms of reference materials we like sites similar to:

http://www.velmarquay.net
http://www.corvidandpine.net
http://www.tessarooms.net
http://www.quillbeds.net

These sites are designed far more simply than large booking sites such as www.roamvix.net, www.bunkfold.net or even wander ledger. However, we are not looking for a copy of the above. We are looking for a design that presents hotels in a novel way and would be seen by the industry as a unique way of displaying new hotels.
Updates

Dear Designers - we have received quite a few entries already. Thank you. However, none of the designs submitted have responded to our brief. They are all copies or derivatives of current hotel websites which is not what we are looking for. We want (a) a new and creative approach to a hotel website and (b) one which creatively uses the age of the hotel (ie. 1 month old, 6 months old etc).

It will require creative thinking and new ideas. We wanted to challenge designers to come up with something new. Thanks.

```html
<!DOCTYPE html>
<html lang="en">
<head>
<meta charset="utf-8">
<title>Brindlestays – Home</title>
<link rel="stylesheet" href="https://fonts.googleapis.com/css2?family=Open+Sans:wght@400&display=swap">
<style>
  :root {
    --page-bg: #f4f6f9;
    --bar-dark: #2a2a2a;
    --brand-blue: #0b52c9;
    --intro-blue: rgba(8, 76, 200, 0.88);
    --link-blue: #6fa0ee;
    --select-blue: #4f86df;
    --panel-frame: rgba(225, 228, 232, 0.55);
    --panel-head: #c4c4c4;
    --row-bg: #f7f8fa;
    --row-line: #d0d3d8;
    --row-text: #7a7d82;
    --panel-foot: #c9c9c9;
    --track: #a9a9a9;
    --white: #ffffff;
    --ink: #333333;
  }
  * { box-sizing: border-box; margin: 0; padding: 0; }
  html, body {
    width: 1200px; height: 882px; overflow: hidden;
    background: var(--page-bg);
    font-family: "Open Sans", sans-serif;
  }
  .site {
    position: absolute; left: 98px; top: 0; width: 1004px; height: 882px;
    background: var(--bar-dark);
  }
  .site-header {
    height: 103px; display: flex; align-items: center; justify-content: center;
  }
  .brand {
    color: var(--white); font-size: 41px; font-weight: 400; letter-spacing: 1px;
  }
  .hero {
    position: absolute; left: 0; top: 103px; width: 1004px; height: 715px; overflow: hidden;
  }
  .hero-photo {
    position: absolute; inset: 0;
    background:
      linear-gradient(160deg, rgba(120,80,40,0) 55%, rgba(140,80,50,0.75) 75%, rgba(90,70,60,0.85) 100%),
      linear-gradient(180deg, #1f5fd0 0%, #4c8fe6 30%, #8fd6e6 52%, #3fc4d0 66%, #1aa7b8 100%);
  }
  .intro {
    position: absolute; left: 0; top: 0; width: 613px; height: 163px;
    background: var(--intro-blue); color: var(--white);
    padding: 24px 0 0 31px;
  }
  .intro-lead { font-size: 19px; line-height: 24px; }
  .intro-lead .site-name { color: var(--link-blue); }
  .intro-sub { font-size: 16px; line-height: 21px; margin-top: 19px; padding-left: 2px; }

  .filter {
    position: absolute; top: 224px; width: 290px; height: 321px;
    background: var(--panel-frame); border-radius: 10px;
  }
  .filter-inner {
    position: absolute; left: 8px; top: 8px; width: 273px; height: 304px;
    background: var(--panel-foot); border-radius: 6px; overflow: hidden;
  }
  .filter-title {
    height: 44px; line-height: 42px; text-align: center;
    background: var(--panel-head); color: var(--ink);
    font-size: 18px; letter-spacing: 0.5px;
    border-bottom: 1px solid #b0b0b0;
  }
  .options { list-style: none; position: relative; }
  .option {
    height: 39px; line-height: 39px; padding-left: 28px;
    background: var(--row-bg); color: var(--row-text); font-size: 17px;
    border-bottom: 1px solid var(--row-line);
    display: flex; align-items: center; gap: 12px;
  }
  .option svg { width: 12px; height: 10px; fill: currentColor; }
  .option.is-selected { background: var(--select-blue); color: var(--white); }
  .option.is-empty { background: var(--row-bg); }
  .has-scroll .option { margin-right: 18px; }
  .scrollbar { position: absolute; right: 0; top: 0; width: 18px; height: 235px; }

  .filter-age { left: 43px; }
  .filter-location { left: 358px; }
  .filter-style { left: 671px; }

  .search-button {
    position: absolute; left: 681px; top: 594px; width: 270px; height: 72px;
    background: var(--brand-blue); color: var(--white);
    font-family: inherit; font-size: 23px; letter-spacing: 1px; border: 0;
  }
  .site-footer { position: absolute; left: 0; top: 818px; width: 1004px; height: 64px; }
</style>
</head>
<body>
<div class="site">
  <header class="site-header">
    <span class="brand">BRINDLESTAYS</span>
  </header>

  <main class="hero">
    <div class="hero-photo" role="img" aria-label="Photo of an overwater thatched villa on a wooden deck above turquoise lagoon water under a blue sky"></div>

    <section class="intro">
      <p class="intro-lead"><span class="site-name">Brindlestays.net</span> lists the world's best new and upcoming hotels leading the way in luxury, design, innovation and service.</p>
      <p class="intro-sub">Explore and book at exclusive opening prices and experience the best new hotels as they open their doors to those in the know.</p>
    </section>

    <section class="filter filter-age">
      <div class="filter-inner">
        <h2 class="filter-title">AGE</h2>
        <ul class="options has-scroll">
          <li class="option is-selected"><svg viewBox="0 0 12 10"><path d="M0 0 12 5 0 10 3 5z"/></svg>1 month</li>
          <li class="option"><svg viewBox="0 0 12 10"><path d="M0 0 12 5 0 10 3 5z"/></svg>2 months</li>
          <li class="option"><svg viewBox="0 0 12 10"><path d="M0 0 12 5 0 10 3 5z"/></svg>3 months</li>
          <li class="option"><svg viewBox="0 0 12 10"><path d="M0 0 12 5 0 10 3 5z"/></svg>4 months</li>
          <li class="option"><svg viewBox="0 0 12 10"><path d="M0 0 12 5 0 10 3 5z"/></svg>5 months</li>
          <li class="option"><svg viewBox="0 0 12 10"><path d="M0 0 12 5 0 10 3 5z"/></svg>6 months</li>
          <svg class="scrollbar" viewBox="0 0 18 235">
            <rect width="18" height="235" fill="#a9a9a9"/>
            <rect x="2" y="3" width="14" height="108" rx="7" fill="#fff" stroke="#8a8a8a"/>
            <path d="M6 15 9 10 12 15z M6 98 9 103 12 98z" fill="#666"/>
            <path d="M5 52h8M5 55h8M5 58h8M5 61h8" stroke="#888"/>
          </svg>
        </ul>
      </div>
    </section>

    <section class="filter filter-location">
      <div class="filter-inner">
        <h2 class="filter-title">LOCATION</h2>
        <ul class="options has-scroll">
          <li class="option"><svg viewBox="0 0 12 10"><path d="M0 0 12 5 0 10 3 5z"/></svg>Alps</li>
          <li class="option"><svg viewBox="0 0 12 10"><path d="M0 0 12 5 0 10 3 5z"/></svg>Bermuda</li>
          <li class="option"><svg viewBox="0 0 12 10"><path d="M0 0 12 5 0 10 3 5z"/></svg>Chile</li>
          <li class="option is-selected"><svg viewBox="0 0 12 10"><path d="M0 0 12 5 0 10 3 5z"/></svg>France</li>
          <li class="option"><svg viewBox="0 0 12 10"><path d="M0 0 12 5 0 10 3 5z"/></svg>Jamaica</li>
          <li class="option"><svg viewBox="0 0 12 10"><path d="M0 0 12 5 0 10 3 5z"/></svg>Laos</li>
          <svg class="scrollbar" viewBox="0 0 18 235">
            <rect width="18" height="235" fill="#a9a9a9"/>
            <rect x="2" y="3" width="14" height="108" rx="7" fill="#fff" stroke="#8a8a8a"/>
            <path d="M6 15 9 10 12 15z M6 98 9 103 12 98z" fill="#666"/>
            <path d="M5 52h8M5 55h8M5 58h8M5 61h8" stroke="#888"/>
          </svg>
        </ul>
      </div>
    </section>

    <section class="filter filter-style">
      <div class="filter-inner">
        <h2 class="filter-title">STYLE</h2>
        <ul class="options">
          <li class="option"><svg viewBox="0 0 12 10"><path d="M0 0 12 5 0 10 3 5z"/></svg>Modern</li>
          <li class="option"><svg viewBox="0 0 12 10"><path d="M0 0 12 5 0 10 3 5z"/></svg>Vintage</li>
          <li class="option"><svg viewBox="0 0 12 10"><path d="M0 0 12 5 0 10 3 5z"/></svg>Spa</li>
          <li class="option is-selected"><svg viewBox="0 0 12 10"><path d="M0 0 12 5 0 10 3 5z"/></svg>Design</li>
          <li class="option is-empty"></li>
          <li class="option is-empty"></li>
        </ul>
      </div>
    </section>

    <button class="search-button" type="button">SEARCH HOTELS</button>
  </main>

  <footer class="site-footer"></footer>
</div>
</body>
</html>
```